VestoraHub.eu - need to polish our homepage (layout only)

We run a website project (http://cz.VestoraHub.eu) enabling free company formations via the Internet.

We now do complete redesign of the website which is almost ready but we still cannot get to proper shape of the homepage and we kindly ask you to participate on finalisation of this.

What we have now:
- design of sub-pages (see attached as NewSubPage design)

What must be preserved on homepage:
- upper horizontal menu and everything above it (logo, sign in button etc.)
- bottom quick navigation menu

What we would like to have (see attached HPSketch):
- unlike current homepage (http://cz.VestoraHub.eu) some introductory section just below the upper horizontal menu which will contain catching words/references

- more detailed website description and left navigation below this introductory section

- right banners stating amount of statutory fees and costs for registered office (if one chooses so)

- section for news

Thank you in advance for your proposals. In case of any queries please let us know.
Updates

Hello designers,

Many thanks for your first proposals, just.two general comments before I comment on particular designs:

1) We will probably want that the website does NOT include images of people but rather keep it as purely informative. The reason is that as we provide free service users often take us as sort of governmental agency and for such it is not very common here to have such type of public images on the website.

2) We will have 2 banners positions for our partners, one 970x200 leaderboard on the top of webpage and one left square below left navigation. You do not need to include them in your proposals, I am just mentioning this that this space must be left free for this purpose.

Many thanks for your effort so far, I will also comment separately on your particular designs.

Lukas

Requirements
Nice to have
• - you may consider substituting bullets in short catching sentences in introductory section by some icons expressing nature of the sentence

```html
<!DOCTYPE html>
<html lang="en">
<head>
<meta charset="utf-8">
<title>VestoraHub.eu – Free company formations online</title>
<link href="https://fonts.googleapis.com/css2?family=Roboto:wght@400;500;700&display=swap" rel="stylesheet">
<style>
:root{
  --blue:#0d5aa7;
  --blue-dark:#0a3f7e;
  --blue-mid:#3f7fc2;
  --green:#3ea61f;
  --green-dark:#2d8614;
  --grey-text:#666;
  --dark:#222;
  --panel:#dce9f5;
  --panel-border:#b7cfe6;
  --box-border:#dcdcdc;
  --footer:#262626;
  --footer-bottom:#141414;
}
*{box-sizing:border-box;margin:0;padding:0}
html,body{width:793px;height:1200px;overflow:hidden;background:#fff;font-family:'Roboto',Arial,sans-serif;color:var(--dark)}
.page{position:relative;width:793px;height:1200px}
.abs{position:absolute}
.partner-leaderboard{left:86px;top:10px;width:620px;height:62px;background:linear-gradient(90deg,#2a1a12,#4a3020,#2a1a12)}
.brand{left:86px;top:92px;font-size:24px;font-weight:700;color:var(--blue);letter-spacing:.3px;display:flex;align-items:center;gap:7px}
.brand-mark{width:18px;height:18px;background:var(--blue)}
.contact{left:406px;top:92px;font-size:9px;color:#888;line-height:15px;letter-spacing:.4px}
.contact div{display:flex;align-items:center;gap:6px}
.btn-account{top:97px;height:19px;font-size:9.5px;color:#fff;display:flex;align-items:center;justify-content:center;border-radius:2px}
.btn-signin{left:574px;width:60px;background:var(--blue)}
.btn-newuser{left:637px;width:69px;background:#9a9a9a}
.mainnav{left:86px;top:137px;width:620px;height:35px;background:linear-gradient(#1466b6,#0a4c94);display:flex;border-radius:1px}
.mainnav .home{width:40px;background:var(--green);display:flex;align-items:center;justify-content:center}
.mainnav a{color:#fff;text-decoration:none;font-size:12px;letter-spacing:.4px;display:flex;align-items:center;justify-content:center;border-right:1px solid #08407e}
.mainnav .tools{margin-left:auto;display:flex;align-items:center;gap:9px;padding-right:12px}
.intro-title{left:86px;top:194px;font-size:16px;color:var(--blue);letter-spacing:.6px;display:flex;align-items:center;gap:8px}
.benefits{left:90px;top:226px;list-style:none;font-size:11.5px;color:var(--grey-text);letter-spacing:.3px}
.benefits li{display:flex;align-items:center;gap:10px;height:20.5px}
.cta{top:326px;height:23px;background:linear-gradient(#4cb52b,var(--green-dark));color:#fff;font-size:9px;font-weight:700;letter-spacing:.5px;display:flex;align-items:center;justify-content:center;border-radius:1px}
.cta-try{left:86px;width:181px}
.cta-how{left:274px;width:96px}
.card{border:1px solid var(--box-border);background:#fbfbfb}
.counter{left:521px;top:196px;width:185px;height:66px;padding:9px 9px}
.counter h3{font-weight:400;font-size:13.5px;color:#777}
.counter .num{margin-top:4px;display:flex;align-items:baseline;gap:5px;color:var(--blue);white-space:nowrap}
.counter .num b{font-size:21px}
.counter .num .unit{font-size:14px}
.counter .num .tag{margin-left:5px;background:var(--green);color:#fff;font-size:8px;font-weight:700;letter-spacing:.5px;padding:4px 7px;align-self:center;line-height:10px}
.testimonials{left:521px;top:270px;width:185px;height:79px;padding:8px 11px}
.testimonials h3{font-weight:400;font-size:13.5px;color:#777}
.testimonials .row{display:flex;align-items:center;justify-content:space-between;margin-top:6px}
.badge{width:42px;height:42px;border-radius:50%;background:#e8eef5;border:1px solid #c8d4e2}
.sidenav{left:86px;top:367px;width:150px;list-style:none}
.sidenav li{height:24px;margin-bottom:5px;background:linear-gradient(#f3f3f3,#e3e3e3);border:1px solid #d4d4d4;font-size:9.5px;font-weight:700;letter-spacing:.6px;color:#333;display:flex;align-items:center;justify-content:center}
.sidenav li.active{background:var(--panel);border-color:var(--panel-border);color:var(--blue-dark);height:23px}
.side-photo{left:86px;top:574px;width:145px;height:127px;background:linear-gradient(135deg,#e9e4de,#9fb0c4 60%,#3d4a5c);border:1px solid #ddd}
.why{left:236px;top:367px;width:270px;height:423px;background:var(--panel);border:1px solid var(--panel-border);padding:10px 20px 0 22px}
.why h2{font-size:15px;font-weight:700;color:#666;letter-spacing:.4px;margin:0 0 11px 0}
.why p{font-size:9px;line-height:12.8px;color:#333;margin-bottom:12.8px;position:relative}
.why p::before{content:"";position:absolute;left:-1px;top:3px;width:4px;height:4px;border-right:1.5px solid var(--blue);border-bottom:1.5px solid var(--blue);transform:rotate(-45deg)}
.why p span{padding-left:8px}
.pricebox{left:521px;width:185px;padding:6px 5px}
.pricebox h3{font-size:12px;font-weight:500;color:var(--blue);letter-spacing:.6px;line-height:15.5px;padding:0 5px 4px}
.pricebox .row{background:var(--blue-mid);color:#fff;height:21px;margin-top:2px;font-size:10px;display:flex;align-items:center;padding:0 5px;letter-spacing:.2px;white-space:nowrap}
.pricebox .row small{font-size:9px;margin:0 4px}
.pricebox .row b{font-size:11.5px}
.pricebox .row .end{margin-left:auto}
.fees{top:367px;height:92px}
.office{top:467px;height:93px}
.news-title{left:86px;top:805px;font-size:19px;color:var(--blue);letter-spacing:.5px;font-weight:400}
.news{top:836px;width:179px}
.news h4{font-size:10.5px;font-weight:700;color:#111;margin-left:1px}
.news .bubble{position:relative;margin-top:7px;height:106px;border:1px solid #d8d8d8;box-shadow:0 0 2px #ddd;padding:15px 12px 0;font-size:9px;line-height:12.8px;color:#333;text-align:center;background:#fff}
.news .bubble::after{content:"";position:absolute;right:44px;bottom:-7px;width:11px;height:11px;background:#fff;border-right:1px solid #d8d8d8;border-bottom:1px solid #d8d8d8;transform:rotate(45deg)}
.news .meta{display:flex;justify-content:flex-end;align-items:center;gap:11px;margin-top:8px;font-size:7.5px;letter-spacing:.6px;color:#333;text-align:center;line-height:10px}
.avatar{width:39px;height:33px;border:1px solid #ccc;padding:2px;background:#fff}
.avatar div{width:100%;height:100%;background:linear-gradient(#8a9aa8,#5a6672)}
.more{left:627px;top:1016px;font-size:10px;font-weight:700;color:var(--blue);text-decoration:underline;letter-spacing:.4px}
.footer{left:0;top:1045px;width:793px;height:133px;background:var(--footer)}
.fcol{top:1075px;color:#fff}
.fcol h5{font-size:12px;font-weight:400;letter-spacing:.4px;padding-bottom:7px;border-bottom:1px solid #3a3a3a;margin-bottom:9px}
.fcol ul{list-style:none;font-size:9px;letter-spacing:.4px;line-height:12.8px;color:#ddd}
.fcol li::before{content:"›";margin-right:7px;color:#fff}
.fcol li.hl{color:var(--green)}
.fsep{top:1072px;width:1px;height:86px;background:#3a3a3a}
.copyright{left:0;top:1178px;width:793px;height:22px;background:var(--footer-bottom);color:#ddd;font-size:7.5px;letter-spacing:.5px;padding:7px 0 0 86px}
</style>
</head>
<body>
<div class="page">

  <div class="abs partner-leaderboard" role="img" aria-label="Partner leaderboard banner"></div>

  <div class="abs brand"><span class="brand-mark"></span>VESTORAHUB.eu</div>

  <div class="abs contact">
    <div><svg width="9" height="9" viewBox="0 0 10 10"><path d="M2 1l2 2-1 1.5c.6 1.2 1.4 2 2.5 2.5L7 6l2 2-1.5 1.5C4.5 9 1 5.5.5 2.5z" fill="#999"/></svg>220 555 018</div>
    <div><svg width="9" height="7" viewBox="0 0 10 7"><rect x=".5" y=".5" width="9" height="6" fill="none" stroke="#999"/><path d="M.5.5l4.5 3.5L9.5.5" fill="none" stroke="#999"/></svg>info@vestorahub.eu</div>
  </div>

  <div class="abs btn-account btn-signin">Sign in</div>
  <div class="abs btn-account btn-newuser">New user</div>

  <nav class="abs mainnav">
    <div class="home"><svg width="18" height="15" viewBox="0 0 18 15"><path d="M9 1L1 8h2.5v6h4V10h3v4h4V8H17z" fill="#fff"/></svg></div>
    <a style="width:118px">Zalozeni S.R.O.</a>
    <a style="width:126px">Zivnostensky list</a>
    <a style="width:104px">Zalozeni A.S</a>
    <div class="tools">
      <svg width="16" height="16" viewBox="0 0 16 16"><circle cx="8" cy="8" r="5" fill="none" stroke="#fff" stroke-width="3" stroke-dasharray="2.6 1.3"/><circle cx="8" cy="8" r="2" fill="#fff"/></svg>
      <svg width="16" height="16" viewBox="0 0 16 16"><circle cx="8" cy="8" r="7.5" fill="#fff"/><text x="8" y="12" text-anchor="middle" font-size="11" font-weight="700" fill="#0d5aa7" font-family="Roboto,Arial,sans-serif">?</text></svg>
      <svg width="20" height="13" viewBox="0 0 20 13"><rect width="20" height="13" fill="#1c3f8a"/><path d="M0 0L20 13M20 0L0 13" stroke="#fff" stroke-width="2.5"/><path d="M0 0L20 13M20 0L0 13" stroke="#c8102e" stroke-width="1"/><path d="M10 0v13M0 6.5h20" stroke="#fff" stroke-width="4"/><path d="M10 0v13M0 6.5h20" stroke="#c8102e" stroke-width="2.2"/></svg>
    </div>
  </nav>

  <h1 class="abs intro-title" style="font-weight:400">
    <svg width="19" height="17" viewBox="0 0 19 17"><rect x="1" y="1" width="17" height="11" fill="none" stroke="#0d5aa7" stroke-width="2"/><path d="M7 15h5M9.5 12v3" stroke="#0d5aa7" stroke-width="2"/></svg>
    FREE COMPANY FORMATIONS ONLINE
  </h1>

  <ul class="abs benefits">
    <li><svg width="15" height="13" viewBox="0 0 15 13"><rect x="1" y="2" width="10" height="10" fill="none" stroke="#3ea61f" stroke-width="1.6"/><path d="M3.5 6.5l3 3 7-8" fill="none" stroke="#3ea61f" stroke-width="2.2"/></svg>Pay statutory registration fees only.</li>
    <li><svg width="15" height="13" viewBox="0 0 15 13"><rect x="1" y="2" width="10" height="10" fill="none" stroke="#3ea61f" stroke-width="1.6"/><path d="M3.5 6.5l3 3 7-8" fill="none" stroke="#3ea61f" stroke-width="2.2"/></svg>Simply without attending state authorities.</li>
    <li><svg width="15" height="13" viewBox="0 0 15 13"><rect x="1" y="2" width="10" height="10" fill="none" stroke="#3ea61f" stroke-width="1.6"/><path d="M3.5 6.5l3 3 7-8" fill="none" stroke="#3ea61f" stroke-width="2.2"/></svg>Registered capital from CZK 1.</li>
    <li><svg width="15" height="13" viewBox="0 0 15 13"><rect x="1" y="2" width="10" height="10" fill="none" stroke="#3ea61f" stroke-width="1.6"/><path d="M3.5 6.5l3 3 7-8" fill="none" stroke="#3ea61f" stroke-width="2.2"/></svg>Company formed in 3-5 days.</li>
  </ul>

  <div class="abs cta cta-try">TRY UNBINDING REGISTRATION</div>
  <div class="abs cta cta-how">HOW IT WORKS</div>

  <div class="abs card counter">
    <h3>Registered up to Date</h3>
    <div class="num"><b>4345</b><span class="unit">firms</span><span class="tag">REGISTRED</span></div>
  </div>

  <div class="abs card testimonials">
    <h3>Testimonails</h3>
    <div class="row">
      <svg width="12" height="20" viewBox="0 0 12 20"><path d="M10 2L2 10l8 8" fill="none" stroke="#ccc" stroke-width="2.5"/></svg>
      <div class="badge" role="img" aria-label="Partner badge"></div>
      <div class="badge" role="img" aria-label="Award badge"></div>
      <svg width="12" height="20" viewBox="0 0 12 20"><path d="M2 2l8 8-8 8" fill="none" stroke="#ccc" stroke-width="2.5"/></svg>
    </div>
  </div>

  <ul class="abs sidenav">
    <li class="active">HOME</li>
    <li>HOW IT WORKS</li>
    <li>BEFORE BEGINNING</li>
    <li>FORM COMPANY</li>
    <li>CHECK REGISTRATION</li>
    <li>FAQ</li>
    <li>CONTACTS</li>
  </ul>

  <div class="abs side-photo" role="img" aria-label="Photo of a person working at a computer"></div>

  <section class="abs why">
    <h2>Why VestoraHub.eu?</h2>
    <p><span>The only system in the Czech Republic nabling the complex formation of new companies online through the Internet, without complicated dministration and running around state authorities.</span></p>
    <p><span>Free of charge handling with the payment of statutory registration fees only. Save 60-80% of costs in comparison with the formation of companies through a law firm or the purchase of a ready-made (shelf) company.</span></p>
    <p><span>Short registration process, all documentation is generated automatically online and the registration is completed in short periods (usually 3- 5 business days).</span></p>
    <p><span>Simple and user-friendly online registration form enabling tailor-made company formation for each user.</span></p>
    <p><span>Free-of-charge online formation of limited liability company (s.r.o.), trade license (ZL) and joint-stock company (a.s.). Possibility of another company forms through individual formation process.</span></p>
    <p><span>Professional legal support during the whole course of the company registration and 100% guarantee of registration in the Company Register.</span></p>
  </section>

  <div class="abs card pricebox fees">
    <h3>STATUTORY COSTS ONLY,<br>NO COMMITMENTS</h3>
    <div class="row">S.R.O.<small>formation from CZK</small><b class="end">13,500</b></div>
    <div class="row">ŽL<small style="margin-left:30px">formation from CZK</small><b class="end">1,000</b></div>
  </div>

  <div class="abs card pricebox office">
    <h3>NEED ALSO REGISTERED<br>OFFICE?</h3>
    <div class="row">Prague<small>from CZK</small><b>216</b>/month</div>
    <div class="row">Ostrava<small>from CZK</small><b>436</b>/month</div>
  </div>

  <h2 class="abs news-title">NEWS</h2>

  <article class="abs news" style="left:86px">
    <h4>Applies to The Startups of.........</h4>
    <div class="bubble">Startups of the Year 2011 is a new competition, designated for starting entrepreneurs where valuable prices and professional support may be found for the start of business. The competition was</div>
    <div class="meta"><div>30. 09. 2011<br>Martin Hale</div><div class="avatar"><div role="img" aria-label="Author portrait"></div></div></div>
  </article>

  <article class="abs news" style="left:306px">
    <h4>The change of court fees...........</h4>
    <div class="bubble">As of 1.9.2011, the change to statutory court fees will become effective for the registration of new companies into the Czech Company Register .<br>Instead of the current CZK 5,000</div>
    <div class="meta"><div>15. 08. 2011<br>Oskar</div><div class="avatar"><div role="img" aria-label="Author portrait"></div></div></div>
  </article>

  <article class="abs news" style="left:527px">
    <h4>Applies to The Startups of.........</h4>
    <div class="bubble">Startups of the Year 2011 is a new competition, designated for starting entrepreneurs where valuable prices and professional support may be found for the start of business. The competition was</div>
    <div class="meta"><div>30. 09. 2011<br>Lena</div><div class="avatar"><div role="img" aria-label="Author portrait" style="background:linear-gradient(#e4c29a,#c98a6a)"></div></div></div>
  </article>

  <a class="abs more">More News.......</a>

  <footer class="abs footer"></footer>
  <div class="abs fcol" style="left:86px;top:1078px;width:108px"><h5>Form Company</h5><ul><li class="hl">S.R.O</li><li>Trade License</li></ul></div>
  <div class="abs fsep" style="left:222px"></div>
  <div class="abs fcol" style="left:259px;width:110px"><h5>Clint Zone</h5><ul><li>My Registrations</li><li>Check Registration</li><li>My Profile</li></ul></div>
  <div class="abs fsep" style="left:390px"></div>
  <div class="abs fcol" style="left:423px;top:1078px;width:127px"><h5>VestoraHub.eu</h5><ul><li>How it Works</li><li>Before Beginnings</li><li>Business Conditions</li><li>Affilate Program</li></ul></div>
  <div class="abs fsep" style="left:577px"></div>
  <div class="abs fcol" style="left:614px;top:1078px;width:92px"><h5>Support</h5><ul><li>Contact</li><li>FAQ</li></ul></div>

  <div class="abs copyright">Copyright © 2014 VestoraHub.eu, all rights reserved</div>
</div>
</body>
</html>
```